We need a poster design for "KEVO Sports Night" events. The events have been around for 3 years and we hope the poster will give a sense of vibrant and active designs. It is more to a community event with teamwork and fun.

I have uploaded a past event poster just FYI.

Target Market(s)

Community, Family

Industry/Entity Type

Non Profit

Logo Text

KEVO Sports Night

Requirements
Must have
• KEVO Sports Night
• Organiser: KEVO Sydney
• Date: 25/11/2017
• Time: 4:00pm
• Venue: Wendamere Park
• Facebook: kevosport

```html
<!DOCTYPE html>
<html lang="en">
<head>
<meta charset="utf-8">
<title>KEVO Sports Night</title>
<link rel="stylesheet" href="https://fonts.googleapis.com/css2?family=Oswald:wght@400;500&family=Fjalla+One&display=swap">
<style>
  :root {
    --bg-top: #b8141d;
    --bg-mid: #6e2545;
    --bg-low: #3a2a5a;
    --bg-bottom: #122a6a;
    --cream: #fffbd2;
    --cream-deep: #fff3a8;
    --orange: #f5a235;
    --white: #ffffff;
    --shard: #d9333b;
  }
  * { margin: 0; padding: 0; box-sizing: border-box; }
  html, body { width: 849px; height: 1200px; overflow: hidden; }
  body { background: var(--bg-bottom); }
  .poster {
    position: relative;
    width: 849px;
    height: 1200px;
    overflow: hidden;
    background: linear-gradient(180deg, var(--bg-top) 0%, var(--bg-mid) 42%, var(--bg-low) 70%, var(--bg-bottom) 100%);
    font-family: "Fjalla One", "Oswald", sans-serif;
    color: var(--white);
  }
  .art { position: absolute; }
  .art--shards {
    left: 0; top: 0; width: 390px; height: 620px;
    background: radial-gradient(ellipse at 25% 35%, rgba(230,60,60,0.55) 0%, rgba(210,45,55,0.3) 45%, rgba(180,30,50,0) 75%);
  }
  .art--kicker {
    left: 140px; top: 10px; width: 260px; height: 230px;
    border-radius: 40% 50% 30% 40%;
    background: radial-gradient(ellipse, rgba(225,55,55,0.55) 0%, rgba(225,55,55,0) 72%);
  }
  .wordmark { position: absolute; left: 0; top: 0; width: 849px; height: 560px; }
  .art--cyclist {
    left: 22px; top: 355px; width: 250px; height: 230px;
    border-radius: 45%;
    background: radial-gradient(ellipse, rgba(200,110,190,0.6) 0%, rgba(150,90,200,0.35) 50%, rgba(150,90,200,0) 75%);
  }
  .art--jumper {
    left: 390px; top: 250px; width: 110px; height: 240px;
    border-radius: 45%;
    background: radial-gradient(ellipse, rgba(230,120,60,0.7) 0%, rgba(120,170,80,0.4) 55%, rgba(120,170,80,0) 78%);
  }
  .ball {
    position: absolute; left: 477px; top: 196px; width: 48px; height: 48px;
    border-radius: 50%;
    background: radial-gradient(circle at 40% 35%, #ffc23a, #f08a14);
  }
  .art--setter {
    left: 530px; top: 420px; width: 235px; height: 200px;
    border-radius: 45%;
    background: radial-gradient(ellipse, rgba(120,200,170,0.6) 0%, rgba(150,110,200,0.4) 55%, rgba(150,110,200,0) 78%);
  }
  .art--tennis {
    left: 690px; top: 265px; width: 159px; height: 265px;
    border-radius: 45% 0 0 45%;
    background: radial-gradient(ellipse at 60% 45%, rgba(250,230,150,0.7) 0%, rgba(240,150,170,0.45) 55%, rgba(240,150,170,0) 80%);
  }
  .tagline {
    position: absolute; left: 0; right: 0; top: 558px;
    text-align: center;
    font-family: "Oswald", sans-serif;
    font-weight: 400;
    font-size: 104px;
    line-height: 1;
    letter-spacing: 2px;
    color: var(--orange);
  }
  .details {
    position: absolute; left: 0; right: 0; top: 806px;
    text-align: center;
    list-style: none;
    font-size: 38px;
    line-height: 1;
  }
  .details li { margin-bottom: 38px; letter-spacing: 0.5px; }
  .organiser {
    position: absolute; left: 0; right: 0; top: 1096px;
    text-align: center;
    font-size: 40px;
    color: var(--orange);
    letter-spacing: 1px;
  }
  .social {
    position: absolute; right: 24px; top: 24px;
    display: flex; align-items: center; gap: 6px;
    font-size: 23px; line-height: 1;
  }
  .social__dot { width: 24px; height: 24px; background: var(--white); border-radius: 3px; }
</style>
</head>
<body>
<main class="poster">
  <div class="art art--shards" role="img" aria-label="Scattered red polygon shards trailing from a leaping athlete"></div>
  <div class="art art--kicker" role="img" aria-label="Red low-poly silhouette of a kicking footballer"></div>

  <svg class="wordmark" viewBox="0 0 849 560" aria-label="KEVO">
    <defs>
      <linearGradient id="cream-fill" x1="0" y1="0" x2="0" y2="1">
        <stop offset="0" stop-color="var(--cream-deep)"/>
        <stop offset="1" stop-color="var(--cream)"/>
      </linearGradient>
    </defs>
    <text x="162" y="535" textLength="556" lengthAdjust="spacingAndGlyphs"
          font-family="Oswald, sans-serif" font-weight="400" font-size="465"
          fill="url(#cream-fill)">KEVO</text>
  </svg>

  <div class="art art--cyclist" role="img" aria-label="Colourful low-poly cyclist on a pink bicycle"></div>
  <div class="art art--jumper" role="img" aria-label="Colourful low-poly basketball player leaping"></div>
  <div class="ball"></div>
  <div class="art art--setter" role="img" aria-label="Colourful low-poly volleyball player with ball"></div>
  <div class="art art--tennis" role="img" aria-label="Colourful low-poly tennis player swinging a racket"></div>

  <h1 class="tagline">Sports Night</h1>

  <ul class="details">
    <li>Date: 25/11/2017</li>
    <li>Time: 4:00pm</li>
    <li>Venue: Wendamere Park</li>
  </ul>

  <p class="organiser">Organiser : KEVO Sydney</p>

  <p class="social"><span class="social__dot"></span>\kevosport</p>
</main>
</body>
</html>
```